The Pixel Tavern Business card.

A Simple card with our Logo and contact information. To give to investors and other professionals.

We are a nerd themed bar.
our target market is young professionals age 21+ but the real purpose of this business card is to present to potential investors and other professionals with our contact information. as we are still looking for funding before we start up.

I am partial to green and my partner likes red we are open to iteration.

Target Market(s)

Investors

Industry/Entity Type

Business

Contact Information for Business Card

Marcus Henley (555) 730-6621 kent.w4100@mailbox-demo.net Brian Tolle (555) 918-2047 briant731@mailbox-demo.net

Font styles to use
Serif

Requirements
Nice to have
• Keep it simple but not boring.
• Use the Logos but feel free to edit them to match theme/colors.
• Keep the back clean and use one of the Logos.

```html
<!DOCTYPE html>
<html lang="en">
<head>
<meta charset="utf-8">
<title>The Pixel Tavern — Business Card</title>
<link rel="stylesheet" href="https://fonts.googleapis.com/css2?family=Cinzel:wght@500;700&family=Open+Sans:wght@400&display=swap">
<style>
  :root {
    --backdrop: #cbcbcb;
    --card: #f5f5f5;
    --ink: #111111;
    --muted: #2a2a2a;
    --divider: #e4e4e4;
    --brand-green: #04933f;
    --brand-red: #d9251c;
  }
  html, body {
    margin: 0;
    padding: 0;
    width: 1200px;
    height: 1005px;
    overflow: hidden;
    background: var(--backdrop);
  }
  .canvas {
    position: relative;
    width: 1200px;
    height: 1005px;
  }
  .card {
    position: absolute;
    left: 280px;
    width: 640px;
    height: 366px;
    background: var(--card);
    box-shadow: 0 3px 8px rgba(0,0,0,0.18);
    overflow: hidden;
  }
  .card--front { top: 90px; }
  .card--back { top: 530px; }

  .brand {
    position: absolute;
    display: flex;
    align-items: center;
    gap: 16px;
    font-family: "Cinzel", serif;
    font-weight: 700;
    color: var(--ink);
    white-space: nowrap;
  }
  .brand__dot {
    flex: none;
    border-radius: 50%;
    background: var(--brand-red);
  }
  .card--front .brand {
    left: 50%;
    top: 50%;
    transform: translate(-50%, -50%);
    font-size: 44px;
    letter-spacing: 1px;
  }
  .card--front .brand__dot { width: 34px; height: 34px; }

  .card--back .brand {
    left: 34px;
    top: 148px;
    font-size: 25px;
    gap: 10px;
  }
  .card--back .brand__dot { width: 20px; height: 20px; }

  .card__divider {
    position: absolute;
    left: 330px;
    top: 0;
    width: 1px;
    height: 300px;
    background: var(--divider);
  }

  .contact {
    position: absolute;
    left: 362px;
    top: 124px;
  }
  .contact__name {
    margin: 0 0 10px;
    font-family: "Cinzel", serif;
    font-weight: 500;
    font-size: 24px;
    color: var(--ink);
    letter-spacing: 0.5px;
  }
  .contact__list {
    list-style: none;
    margin: 0;
    padding: 0;
    font-family: "Open Sans", sans-serif;
    font-size: 15px;
    color: var(--muted);
  }
  .contact__item {
    display: flex;
    align-items: center;
    gap: 12px;
    line-height: 24px;
  }
  .contact__icon { width: 14px; height: 12px; flex: none; }

  .card__bands {
    position: absolute;
    left: 0;
    bottom: 0;
    width: 640px;
    height: 70px;
  }
</style>
</head>
<body>
<main class="canvas">
  <section class="card card--front" aria-label="Card front">
    <div class="brand">
      <span class="brand__dot"></span>
      <span class="brand__name">The Pixel Tavern</span>
    </div>
  </section>

  <section class="card card--back" aria-label="Card back">
    <div class="brand">
      <span class="brand__dot"></span>
      <span class="brand__name">The Pixel Tavern</span>
    </div>

    <div class="card__divider"></div>

    <div class="contact">
      <h1 class="contact__name">Marcus Henley</h1>
      <ul class="contact__list">
        <li class="contact__item">
          <svg class="contact__icon" viewBox="0 0 14 12" aria-hidden="true">
            <path d="M1 4 C1 1 13 1 13 4 L11 5 L10 3.5 L4 3.5 L3 5 Z" fill="var(--brand-green)"/>
            <rect x="3" y="5.5" width="8" height="5.5" rx="1" fill="var(--brand-green)"/>
          </svg>
          <span>(555) 730-6621</span>
        </li>
        <li class="contact__item">
          <svg class="contact__icon" viewBox="0 0 14 12" aria-hidden="true">
            <rect x="0.5" y="1.5" width="13" height="9" fill="var(--brand-red)"/>
            <path d="M0.5 1.5 L7 7 L13.5 1.5" fill="none" stroke="#ffffff" stroke-width="1"/>
          </svg>
          <span>kent.w4100@mailbox-demo.net</span>
        </li>
      </ul>
    </div>

    <svg class="card__bands" viewBox="0 0 640 70" aria-hidden="true">
      <rect x="0" y="52" width="340" height="18" fill="var(--brand-green)"/>
      <polygon points="348,20 640,20 640,70 326,70" fill="var(--brand-red)"/>
    </svg>
  </section>
</main>
</body>
</html>
```